I need a SEO-friendly Wordpress website (making sure to style H1, H2, H3, etc correctly) for a Hawaii-based law firm called Meridale Crown Legal Group. Comparable websites include https://brvtlaw.com/ and https://www.lorvin.com/ for design reference. The current copy on the TuvellAttorney.com website can be used.

Coding

Coded - Design and coding required

```html
<!DOCTYPE html>
<html lang="en">
<head>
<meta charset="utf-8">
<title>Meridale Crown Legal Group — Kona Lawyers</title>
<link href="https://fonts.googleapis.com/css2?family=Lora:ital,wght@0,400;0,500;0,600;0,700;1,400&family=Poppins:wght@400;500;600&display=swap" rel="stylesheet">
<style>
:root{
  --yellow:#ffc72c;
  --dark:#2b2d31;
  --ink:#1e1e1e;
  --text:#333;
  --header-bg:#f4f6f9;
  --about-bg:#f1eee9;
  --footnav-bg:#c8c7c3;
  --footer-bg:#f4f6f9;
  --bar:#333436;
  --tip-bg:#f4f5f7;
  --map:#e6e8e7;
}
*{box-sizing:border-box;margin:0;padding:0}
html,body{width:895px;height:1200px;overflow:hidden;background:#fff}
body{position:relative;font-family:'Poppins',sans-serif;color:var(--text)}
.abs{position:absolute}

.topbar{left:0;top:0;width:895px;height:29px;background:var(--yellow)}
.topbar .phone{left:175px;top:8px;font-size:8.5px;font-weight:500;color:var(--ink);display:flex;align-items:center;gap:8px}
.topbar .search{left:678px;top:0;width:30px;height:29px;background:var(--dark);display:flex;align-items:center;justify-content:center}

.site-header{left:0;top:29px;width:895px;height:59px;background:var(--header-bg)}
.brand{left:178px;top:12px}
.brand .name{font-family:'Lora',serif;font-weight:700;font-size:15px;color:var(--ink)}
.brand .tag{font-size:7px;letter-spacing:1.1px;color:#444;margin-top:3px}
.main-nav a{position:absolute;top:0;height:59px;line-height:59px;font-family:'Lora',serif;font-size:7.3px;color:#222;text-decoration:none;letter-spacing:.3px}
.main-nav a.active{background:var(--yellow);font-weight:700;text-align:center;width:43px}

.hero{left:0;top:88px;width:895px;height:302px;background:linear-gradient(100deg,#3b3025 0%,#6b5a45 35%,#9a8a70 60%,#4a4a52 100%)}
.hero-band{left:0;top:325px;width:895px;height:65px;background:rgba(40,38,36,.78);text-align:center}
.hero-band h1{font-family:'Lora',serif;font-size:16px;font-weight:700;color:var(--yellow);letter-spacing:1px;margin-top:12px}
.hero-band h1 span{font-size:11.5px;font-weight:400}
.hero-band p{font-family:'Lora',serif;font-style:italic;font-size:11px;color:#fff;margin-top:5px}

.share{left:0;top:144px;width:21px}
.share div{width:21px;height:21px;margin-bottom:1.5px}

.about{left:0;top:390px;width:895px;height:274px;background:var(--about-bg)}
.about .kicker{left:176px;top:14px;font-family:'Lora',serif;font-size:8px;color:#333}
.about h2{position:absolute;left:176px;top:25px;font-family:'Lora',serif;font-size:14px;font-weight:500;color:var(--ink)}
.about h3{position:absolute;left:176px;top:60px;font-size:7.3px;font-weight:600;color:var(--ink)}
.about p{position:absolute;left:176px;width:452px;font-size:7.5px;line-height:13px;color:#333}
.btn{left:176px;top:211px;width:103px;height:28px;background:var(--dark);color:#fff;font-size:7.3px;font-weight:500;display:flex;align-items:center;justify-content:center}
.experience{left:646px;top:0;width:80px;height:274px;background:var(--yellow)}
.experience .rot{position:absolute;left:40px;top:137px;transform:translate(-50%,-50%) rotate(-90deg);white-space:nowrap;font-family:'Lora',serif;color:var(--ink);display:flex;align-items:flex-end;gap:2px}
.experience .num{font-size:25px;font-weight:700;line-height:1}
.experience .stack{display:flex;flex-direction:column;line-height:1}
.experience .small{font-size:12px;font-weight:700}
.experience .big{font-size:26px;font-weight:700;letter-spacing:.5px}

.card{top:682px;width:271px;height:152px;color:#fff;padding:24px 20px}
.card h2{font-family:'Lora',serif;font-size:14px;font-weight:600;margin-bottom:10px}
.card p{font-size:7.2px;line-height:11.2px}
.card ul{list-style:none}
.card li{font-size:8px;line-height:18.5px;display:flex;align-items:center;gap:6px}
.card li::before{content:"";width:4px;height:4px;border:1.3px solid var(--yellow);border-radius:50%}
.presence{left:167px;background:#5d6065}
.practice{left:456px;background:linear-gradient(90deg,#2b1f18 0%,#4a3124 60%,#6a4a30 100%)}

.tip{top:857px;width:270px;height:73px;background:var(--tip-bg)}
.tip .label{position:absolute;left:0;top:0;width:68px;height:73px;background:var(--yellow)}
.tip .label span{position:absolute;left:34px;top:36px;transform:translate(-50%,-50%) rotate(-90deg);font-family:'Lora',serif;font-weight:700;font-size:12.5px;line-height:12px;text-align:center;color:var(--ink);white-space:nowrap}
.tip .title{position:absolute;left:85px;top:20px;font-size:10.5px;font-weight:500;line-height:17px;color:#222;letter-spacing:.3px}

.foot-nav{left:0;top:954px;width:895px;height:27px;background:var(--footnav-bg)}
.foot-nav a{position:absolute;top:0;line-height:27px;font-family:'Lora',serif;font-size:7.3px;color:#333;text-decoration:none}
.foot-nav a.active{font-weight:700;color:#111}

.footer{left:0;top:981px;width:895px;height:191px;background:var(--footer-bg)}
.footer .org{left:167px;top:26px;font-family:'Lora',serif;font-size:11.5px;color:var(--ink);line-height:14px}
.footer .org b{font-weight:600}
.footer .info{left:168px;font-size:7.5px;line-height:11.3px;color:#333}
.map-frame{left:369px;top:9px;width:357px;height:164px;background:#fff;padding:6px}
.map{width:100%;height:100%;background:var(--map)}

.bottom-bar{left:0;top:1172px;width:895px;height:28px;background:var(--bar)}
.bottom-bar .copy{left:174px;top:10px;font-size:6.5px;color:#ddd}
.bottom-bar .soc{top:7px;width:15px;height:15px}
</style>
</head>
<body>

<div class="abs topbar">
  <div class="abs phone">
    <svg width="9" height="9" viewBox="0 0 24 24"><path d="M6.6 10.8c1.4 2.8 3.8 5.1 6.6 6.6l2.2-2.2c.3-.3.7-.4 1-.2 1.1.4 2.3.6 3.6.6.6 0 1 .4 1 1V20c0 .6-.4 1-1 1C10.6 21 3 13.4 3 4c0-.6.4-1 1-1h3.5c.6 0 1 .4 1 1 0 1.3.2 2.5.6 3.6.1.3 0 .7-.2 1L6.6 10.8z" fill="#1e1e1e"/></svg>
    Call Us: +1.808.555.0142
  </div>
  <div class="abs search">
    <svg width="9" height="9" viewBox="0 0 24 24"><circle cx="10" cy="10" r="6.5" stroke="#fff" stroke-width="3" fill="none"/><path d="M15 15l6 6" stroke="#fff" stroke-width="3"/></svg>
  </div>
</div>

<header class="abs site-header">
  <div class="abs brand">
    <div class="name">Meridale Crown Legal Group</div>
    <div class="tag">DIVORCE AND PERSONAL INJURY LAWYERS</div>
  </div>
  <nav class="main-nav">
    <a class="active" style="left:438px">HOME</a>
    <a style="left:489px">PRACTICE AREAS</a>
    <a style="left:575px">ATTORNEYS</a>
    <a style="left:634px">BLOG</a>
    <a style="left:676px">CONTACT</a>
  </nav>
</header>

<section class="abs hero" role="img" aria-label="Photo of lawyers' hands at a desk with a gavel, law books and documents"></section>
<div class="abs hero-band">
  <h1>KONA LAWYERS OF MCLG <span>- LEGAL KŌKUA WITH ALOHA.</span></h1>
  <p>Over 70 years of combined practice ensure you the best professional service</p>
</div>

<div class="abs share">
  <div style="background:#3b5998"></div>
  <div style="background:#1da1f2"></div>
  <div style="background:#7a8a8c"></div>
  <div style="background:#848484"></div>
  <div style="background:#ff6550"></div>
</div>

<section class="abs about">
  <div class="abs kicker">about the</div>
  <h2>Kona Lawyers of MCLG</h2>
  <h3>Lawyers Serving the Big Island and Neighboring Islands</h3>
  <p style="top:91px">The experienced attorneys in the Meridale Crown Legal Group's Kailua Kona, Hawaii office provide clients with a wide range of litigation expertise, including legal claims involving divorce &amp; family, personal injury, toxic exposures, intellectual property, and real estate.</p>
  <p style="top:143px">Our Kona office also offers commercial and hospitality litigation expertise on behalf of a wide variety of clients, including restaurants, hotels, property owners, and many others. We never wish to see our clients go to court, though if there is no other option, you're in safe hands with our seasoned trial lawyers and the many years of courtroom experience behind them.</p>
  <div class="abs btn">KNOW MORE</div>
  <div class="abs experience">
    <div class="rot"><span class="num">70</span><span class="stack"><span class="small">years of combined</span><span class="big">EXPERIENCE</span></span></div>
  </div>
</section>

<div class="abs card presence" role="img" aria-label="Faded street map background">
  <h2>Nationwide Law Firm Presence</h2>
  <p>Kailua Kona serves as the firm's West Coast headquarters for litigation and representation on behalf of individuals and corporations involved in a wide range of legal matters. The firm and its attorneys are licensed to practice and represent clients in Hawaii, California, Arizona, Texas, and Washington D.C</p>
</div>
<div class="abs card practice" role="img" aria-label="Close-up of a gavel on a dark background">
  <h2>Area of Practice</h2>
  <ul>
    <li>Family &amp; Divorce</li>
    <li>Personal Injury</li>
    <li>Corporate &amp; Intellectual Property</li>
    <li>Real Estate</li>
  </ul>
</div>

<div class="abs tip" style="left:167px">
  <div class="label"><span>Special<br>Tips</span></div>
  <div class="title">Top 10 things to do before<br>filing for a divorce</div>
</div>
<div class="abs tip" style="left:456px">
  <div class="label"><span>Special<br>Tips</span></div>
  <div class="title">Top 10 Things to Do During<br>Custody Battle</div>
</div>

<nav class="abs foot-nav">
  <a class="active" style="left:298px">HOME</a>
  <a style="left:349px">PRACTICE AREAS</a>
  <a style="left:444px">ATTORNEYS</a>
  <a style="left:511px">BLOG</a>
  <a style="left:562px">CONTACT</a>
</nav>

<footer class="abs footer">
  <div class="abs org">Kona Lawyers of<br><b>Meridale Crown Legal Group</b></div>
  <div class="abs info" style="top:75px">75-4100 Alii Kai Road, Suite 210<br>Kailua Kona, Hawaii 96740.</div>
  <div class="abs info" style="top:112px">T:&nbsp;&nbsp;+1.808.555.0142</div>
  <div class="abs info" style="top:135px">clients@tuvellattorney.com<br>www.tuvellattorney.com</div>
  <div class="abs map-frame">
    <div class="map" role="img" aria-label="Street map of Kailua Kona showing the office location"></div>
  </div>
</footer>

<div class="abs bottom-bar">
  <div class="abs copy">Copyright © Meridale Crown Legal Group. All Rights Reserved.</div>
  <div class="abs soc" style="left:644px;background:#3b5998"></div>
  <div class="abs soc" style="left:664px;background:#1da1f2"></div>
  <div class="abs soc" style="left:684px;background:#dd4b39"></div>
  <div class="abs soc" style="left:705px;background:#0e76a8"></div>
</div>

</body>
</html>
```